Postcard Design

I need a postcard/flyer designed to advertise my nail business. I am qualified with Palm and Polish Academy UK and insured with QERVOL. I am offering Lustrea nail

I am fully mobile with flexible appointments. Beautiful nails for up to 3 weeks. No chipping, dulling or fading.

Prices: Fingernails £20. Toenails £20. Both for £35. Gel removal £10

Call Moira on 07812604731 or email lustrea_nails@brivomail.com can also follow on Twitter @Lustrea_nails.

Was hoping for a colourful and classy design, maybe a bit vintage that will appeal to all ages. Especially for weddings/honeymoons. Doesnt necessarily have to feature pictures of manicures/pedicures/hands/feet etc.

hope this all makes sense!

Moira

Industry/Entity Type

Business

Font styles to use
Serif

Colors
e567a6
34b8a4
33a6d7
b768aa
86cfc6
f04a50
d3a5cc

```html
<!DOCTYPE html>
<html lang="en">
<head>
<meta charset="utf-8">
<title>Lustrea Nails – Postcard</title>
<link rel="stylesheet" href="https://fonts.googleapis.com/css2?family=EB+Garamond:wght@400;500&display=swap">
<style>
  :root {
    --teal: #27b8a4;
    --coral: #ea5350;
    --white: #ffffff;
    --rose: #e9a3b4;
    --rose-deep: #c9657e;
    --leaf: #a9c49a;
    --leaf-grey: #7f9a97;
  }
  html, body {
    margin: 0;
    padding: 0;
    width: 1200px;
    height: 836px;
    overflow: hidden;
    background: var(--teal);
  }
  .postcard {
    position: relative;
    width: 1200px;
    height: 836px;
    background: var(--teal);
    font-family: "EB Garamond", Garamond, serif;
    overflow: hidden;
  }
  .floral {
    position: absolute;
  }
  .floral--top-left {
    left: 0;
    top: 0;
    width: 430px;
    height: 358px;
    border-bottom-right-radius: 70% 80%;
    background: radial-gradient(ellipse at 40% 35%, #f1c6cf 0%, var(--rose) 30%, var(--leaf) 62%, rgba(127,154,151,0) 100%);
  }
  .floral--bottom-right {
    right: 0;
    bottom: 0;
    width: 306px;
    height: 292px;
    border-top-left-radius: 80% 75%;
    background: radial-gradient(ellipse at 60% 60%, #f6dde2 0%, var(--rose-deep) 32%, var(--leaf) 64%, rgba(127,154,151,0) 100%);
  }
  .credentials {
    position: absolute;
    right: 34px;
    top: 26px;
    margin: 0;
    text-align: right;
    color: var(--coral);
    font-size: 19px;
    line-height: 36px;
  }
  .headline {
    position: absolute;
    left: 317px;
    width: 600px;
    top: 160px;
    margin: 0;
    text-align: center;
    color: var(--white);
    font-size: 25px;
    font-weight: 400;
    line-height: 40px;
    letter-spacing: 0.3px;
  }
  .price-frame {
    position: absolute;
    left: 360px;
    top: 282px;
    width: 514px;
    height: 392px;
  }
  .price-list {
    position: absolute;
    left: 317px;
    width: 600px;
    top: 364px;
    margin: 0;
    padding: 0;
    list-style: none;
    text-align: center;
    color: var(--white);
    font-size: 46px;
    line-height: 55px;
  }
  .contact {
    position: absolute;
    left: 29px;
    top: 580px;
  }
  .contact__name {
    margin: 0 0 4px 63px;
    color: var(--coral);
    font-size: 54px;
    font-weight: 400;
    line-height: 70px;
  }
  .contact__row {
    display: flex;
    align-items: center;
    height: 52px;
    color: var(--coral);
    font-size: 34px;
  }
  .contact__icon {
    width: 46px;
    height: 46px;
    margin-right: 17px;
    flex: none;
  }
</style>
</head>
<body>
<main class="postcard">
  <div class="floral floral--top-left" role="img" aria-label="Vintage pink roses and blossoms with green leaves"></div>
  <div class="floral floral--bottom-right" role="img" aria-label="Vintage pink and white roses with green leaves"></div>

  <p class="credentials">
    I am qualified with Palm and Polish Academy UK<br>
    and insured with QERVOL.<br>
    I am fully mobile with flexible appointments
  </p>

  <h1 class="headline">
    BEAUTIFUL GEL NAILS<br>
    NO CHIPPING, DULLING OR FADING<br>
    FOR UP TO THREE WEEKS
  </h1>

  <svg class="price-frame" viewBox="0 0 514 392" aria-hidden="true">
    <rect x="6" y="6" width="502" height="380" rx="40" fill="none" stroke="var(--coral)" stroke-width="3"/>
    <rect x="22" y="22" width="470" height="348" rx="28" fill="none" stroke="var(--coral)" stroke-width="2" stroke-dasharray="2 6" stroke-linecap="round"/>
  </svg>

  <ul class="price-list">
    <li>Fingernails £20</li>
    <li>Toenails £20</li>
    <li>Both for £35</li>
    <li>Gel removal £10</li>
  </ul>

  <section class="contact">
    <h2 class="contact__name">Moira</h2>
    <div class="contact__row">
      <svg class="contact__icon" viewBox="0 0 46 46" aria-hidden="true">
        <rect width="46" height="46" fill="var(--coral)"/>
        <rect x="16" y="9" width="14" height="28" rx="2.5" fill="none" stroke="var(--white)" stroke-width="2.5"/>
        <circle cx="23" cy="33" r="1.4" fill="var(--white)"/>
      </svg>
      <span>07812604731</span>
    </div>
    <div class="contact__row">
      <svg class="contact__icon" viewBox="0 0 46 46" aria-hidden="true">
        <rect width="46" height="46" fill="var(--coral)"/>
        <rect x="11" y="14" width="24" height="18" fill="none" stroke="var(--white)" stroke-width="2.5"/>
        <path d="M11 14 L23 24 L35 14" fill="none" stroke="var(--white)" stroke-width="2.5"/>
      </svg>
      <span>lustrea_nails@brivomail.com</span>
    </div>
    <div class="contact__row">
      <svg class="contact__icon" viewBox="0 0 46 46" aria-hidden="true">
        <rect width="46" height="46" fill="var(--coral)"/>
      </svg>
      <span>@Lustrea_nails.</span>
    </div>
  </section>
</main>
</body>
</html>
```